Corporate flyer highlighting service offering for PR agency

A corporate flyer is needed for a new service offering that we are doing. The product name is HarborLeap it is a marketing and communications services offering for companies who are getting ready to sell their business. If we are really happy with the designer's work, there will be a great deal more projects. I am looking for a clean design with a few pops of color from my site. https://quillmarsh.partners. I am looking for a good design with data in sections. I am looking for a clean design that feels high-end but not cluttered. Please do not use images of people. Please see the following examples of types of designs I like.
https://www.tackboard.example/pin/839201746530918264/
https://www.tackboard.example/pin/402918375561029847/
https://assets.stockvale.example/corporate-flyer-template-KRTPMB
https://designbrook.example/item/corporate-flyer-template/81046395?s_rank=8
https://assets.stockvale.example/corporate-business-flyer-template-93PX7D

I had to place the project on hold as I choose the wrong type of project and did not get many designs as a result. I am reposting this with an updated brief.

Target Market(s)

Business sellers and brokers

Industry/Entity Type

Marketing for business sellers

Font styles to use
Sans Serif

Requirements
Must have
• Good quality design with content in sections. Clean and high end feeling is a must.
Should not have
• A lot of images of people.

```html
<!DOCTYPE html>
<html lang="en">
<head>
<meta charset="utf-8">
<title>HarborLeap Flyer – Quillmarsh Partners</title>
<link href="https://fonts.googleapis.com/css2?family=Montserrat:wght@400;600;700;800&family=Open+Sans:wght@400;600;700&display=swap" rel="stylesheet">
<style>
:root{
  --blue:#1d5ea8;
  --blue-dark:#123f73;
  --orange:#f26a21;
  --green:#5fae46;
  --green-light:#eaf4e4;
  --ink:#33393f;
  --muted:#6b737b;
  --paper:#ffffff;
  --bg:#eef1f4;
}
*{box-sizing:border-box;margin:0;padding:0}
html,body{width:1200px;height:2720px;overflow:hidden;background:var(--bg)}
body{font-family:"Open Sans",Arial,sans-serif;color:var(--ink);font-size:14px;line-height:1.5}
h1,h2,h3,.brand{font-family:"Montserrat",Arial,sans-serif}
.page{position:relative;width:1200px;height:1360px;background:var(--paper);overflow:hidden}
.abs{position:absolute}

/* front page */
.brand{display:flex;align-items:center;gap:12px;font-weight:700;font-size:22px;color:var(--blue-dark);letter-spacing:1px}
.brand-mark{width:26px;height:26px;background:var(--orange)}
.hero-photo{left:600px;top:0;width:600px;height:400px;background:linear-gradient(135deg,#8fa7bd,#3f5f80 60%,#223a55)}
.hero-stripe{left:0;top:400px;width:1200px;height:12px;background:var(--blue)}
.title{left:60px;top:120px;width:520px}
.title .lead{color:var(--orange);font-weight:800;font-size:36px;line-height:1.05}
.title .main{color:var(--blue);font-weight:800;font-size:40px;line-height:1.05;margin-top:6px}
.title .sub{color:var(--blue-dark);font-weight:700;font-size:20px;line-height:1.25;margin-top:18px;text-transform:uppercase}
.title .sub span{color:var(--orange)}
.body-col{left:60px;top:450px;width:560px}
.body-col p{margin-bottom:14px}
.body-col h3{color:var(--blue);font-size:18px;margin:6px 0 8px}
.bullet-grid{display:grid;grid-template-columns:1fr 1fr;gap:4px 30px;list-style:none;margin:8px 0 14px}
.bullet-grid li{position:relative;padding-left:16px}
.bullet-grid li::before{content:"";position:absolute;left:0;top:8px;width:7px;height:7px;background:var(--orange)}
.quote-box{left:660px;top:450px;width:480px;height:300px;background:var(--orange);color:#fff;padding:36px 34px}
.quote-box .mark{font-family:"Montserrat",sans-serif;font-size:60px;line-height:.6;font-weight:800}
.quote-box p{font-size:17px;line-height:1.5;margin-top:14px}
.valuation{left:660px;top:780px;width:480px}
.valuation h3{color:var(--green);font-size:18px;margin-bottom:10px}
.tick-list{list-style:none}
.tick-list li{display:flex;gap:10px;align-items:flex-start;margin-bottom:8px}
.tick-list svg{flex:none;margin-top:3px}
.green-band{left:0;top:1040px;width:1200px;height:200px;background:var(--green);color:#fff;padding:36px 60px;display:flex;gap:60px}
.green-band h3{font-size:22px;line-height:1.25;width:420px}
.green-band p{flex:1;font-size:15px}
.footer{left:0;width:1200px;height:80px;background:var(--blue);color:#fff;display:flex;align-items:center;justify-content:flex-end;padding:0 60px;font-family:"Montserrat",sans-serif;font-weight:700;font-size:18px;gap:12px}
.footer .dot{width:12px;height:12px;background:var(--orange)}

/* back page */
.col{top:60px;width:345px}
.col h2{font-size:20px;color:var(--blue);margin-bottom:10px}
.col h3{font-size:15px;color:var(--blue-dark);margin:12px 0 6px}
.col p{margin-bottom:10px;font-size:13.5px}
.service-panel{left:40px;top:40px;width:360px;height:840px;background:var(--green-light);border-left:8px solid var(--green)}
.service-panel .inner{padding:24px 24px}
.service-panel h3{color:var(--green);font-size:15px;margin:14px 0 6px}
.service-panel p{font-size:13px;margin-bottom:6px}
.quote-back{background:var(--orange);color:#fff;padding:22px 24px;margin-top:16px;font-size:15px}
.quote-back cite{display:block;margin-top:8px;font-style:normal;font-weight:700}
.plan-band{left:0;top:920px;width:1200px;height:330px;background:var(--blue);color:#fff}
.plan-text{left:60px;top:950px;width:560px;color:#fff}
.plan-text h3{font-size:20px;margin:10px 0 6px}
.plan-text p{font-size:14px}
.city-photo{left:660px;top:920px;width:540px;height:330px;background:linear-gradient(180deg,#b8c9d9,#6f8aa5 55%,#2f4864)}
</style>
</head>
<body>

<section class="page front">
  <div class="abs brand" style="left:60px;top:44px"><span class="brand-mark"></span>QUILLMARSH PARTNERS</div>
  <div class="abs hero-photo" role="img" aria-label="Photo of two executives in a meeting, framed in a honeycomb pattern"></div>
  <div class="abs title">
    <h1 class="lead">HARBORLEAP PROVIDES</h1>
    <div class="main">EXECUTIVES AND BUSINESS OWNERS WITH</div>
    <div class="sub">Clear guidance to <span>unlock non-financial value</span> ahead of an exit.</div>
  </div>
  <div class="abs hero-stripe"></div>

  <div class="abs body-col">
    <p>Highlighting your company's unique value proposition is key to attracting the right buyers. HarborLeap helps owners shape the story their business tells before it goes to market.</p>
    <p>Understanding how your brand, reputation and relationships are perceived can strengthen valuation and give buyers confidence in the future of the company they acquire.</p>
    <h3>About us</h3>
    <p>Our team of communications specialists has guided founders through strategic transitions for years. We focus on the assets that do not appear on a balance sheet:</p>
    <ul class="bullet-grid">
      <li>Company story</li><li>Brand equity</li>
      <li>Reputation</li><li>Client relationships</li>
      <li>Culture</li><li>Leadership presence</li>
    </ul>
    <p>Each engagement is tailored to your timeline, so owners can prepare with clarity and enter negotiations from a position of strength.</p>
  </div>

  <div class="abs quote-box">
    <div class="mark">“</div>
    <p>Non-financial value drivers often separate a good sale from a great one. Buyers pay for confidence, and confidence is built through clear, consistent communication long before an exit.</p>
  </div>

  <div class="abs valuation">
    <h3>We help companies increase valuation by:</h3>
    <ul class="tick-list">
      <li><svg width="16" height="16" viewBox="0 0 16 16"><path d="M2 8l4 4 8-9" fill="none" stroke="var(--green)" stroke-width="2.5"/></svg>Highlighting value in a clear and visible way</li>
      <li><svg width="16" height="16" viewBox="0 0 16 16"><path d="M2 8l4 4 8-9" fill="none" stroke="var(--green)" stroke-width="2.5"/></svg>Streamlining the exit process</li>
      <li><svg width="16" height="16" viewBox="0 0 16 16"><path d="M2 8l4 4 8-9" fill="none" stroke="var(--green)" stroke-width="2.5"/></svg>Identifying potential risks and suggesting mitigation measures</li>
      <li><svg width="16" height="16" viewBox="0 0 16 16"><path d="M2 8l4 4 8-9" fill="none" stroke="var(--green)" stroke-width="2.5"/></svg>Creating a unified presence in the market ahead of your transition</li>
    </ul>
  </div>

  <div class="abs green-band">
    <h3>Preparing to sell? Start shaping your story now.</h3>
    <p>The earlier you begin, the more value you can reveal. We work alongside owners, brokers and advisors to make sure every stakeholder sees the full worth of the business.</p>
  </div>

  <div class="abs footer" style="top:1280px"><span class="dot"></span>quillmarsh.partners</div>
</section>

<section class="page back">
  <div class="abs service-panel">
    <div class="inner">
      <h2 style="color:var(--blue);font-size:20px;font-family:Montserrat,sans-serif">Our Services</h2>
      <h3>Brand Analysis and Recommendations</h3>
      <p>We review how your brand is seen by clients, staff and the market, then outline clear steps to strengthen it.</p>
      <h3>Customer and Market Perception</h3>
      <p>Interviews and surveys reveal what buyers will learn when they speak to your customers.</p>
      <h3>Employee Engagement</h3>
      <p>A committed team is a selling point. We help communicate change with care and clarity.</p>
      <h3>Reputation Management</h3>
      <p>We identify risks in media and online channels and prepare responses before they matter.</p>
      <h3>Messaging and Content Strategy</h3>
      <p>Consistent messages across your website, materials and leadership voice build buyer trust.</p>
    </div>
  </div>

  <div class="abs col" style="left:430px">
    <h2>We provide</h2>
    <p>HarborLeap delivers communication support that turns intangible strengths into visible, credible value for buyers.</p>
    <p>We begin with an honest look at where you stand and build a focused plan that fits your timeline and goals.</p>
    <h3>Digital and Traditional Marketing</h3>
    <p>From website refresh to thought leadership and media relations, we position the company as a leader in its field.</p>
    <h3>Analysis and Recommendations</h3>
    <p>Clear reports summarise findings and rank actions by their likely effect on value.</p>
    <p>Our process keeps owners informed at every stage and supports brokers with materials that tell a strong story.</p>
  </div>

  <div class="abs col" style="left:815px">
    <h2>Who Has Been Our Success</h2>
    <p>We have worked with founders in professional services, technology, manufacturing and healthcare, each preparing for a sale or succession.</p>
    <p>Our clients value a partner who understands both the emotional and strategic sides of an exit.</p>
    <div class="quote-back">“Strategy without tactics is the slowest route to victory. Tactics without strategy is the noise before defeat.”<cite>— Aren Volk</cite></div>
  </div>

  <div class="abs plan-band"></div>
  <div class="abs plan-text">
    <p>Every HarborLeap engagement follows two clear phases so owners always know what comes next.</p>
    <h3>Gap Assessment</h3>
    <p>We measure brand, reputation and communication against what buyers expect and highlight the gaps that could reduce value.</p>
    <h3>Strategic Roadmap</h3>
    <p>A prioritised plan with timelines and owners that closes those gaps before the business goes to market.</p>
  </div>
  <div class="abs city-photo" role="img" aria-label="Photo of a city skyline with office towers"></div>

  <div class="abs footer" style="top:1280px;justify-content:space-between">
    <span style="display:flex;align-items:center;gap:12px"><span class="dot"></span>info@quillmarsh.partners</span>
    <span>quillmarsh.partners</span>
  </div>
</section>

</body>
</html>
```